Tot Petal Product Label for Tear-Free Head-to-Toe Wash

Need a bottle label design for a new line of natural products targeting infants and children. Products are Pediatrician-developed and paraben-free, sulfate-free, fragrance-free, and cruelty-free. Design should be clean and have a high-end feel to it. Will need other product labels in Tot Petal line designed as well in upcoming projects.

Target Market(s)

Newborn to young elementary age children and their parents

Industry/Entity Type

Cosmetics/Beauty

Font styles to use
Other font styles liked:
• Brand fonts are Jost and Sonorous

Colors

Designer to choose colors to be used in the design.

Requirements
Must have
• Tot Petal logo, Pediatrician Developed logo, and a clean high-end feel to it. The label must fit the specialty bottle we will be using (label measurements and diagram will be provided) for the front and back of bottle only (NOT the side labels). It must include our list of ingredients (will provide once designer selected).
Nice to have
• Should stand out on the shelf of other baby products due to it's clean simplicity and high-end feel
Should not have
• too much of a "kiddie" feel to it (targeting the parents not the kids)

```html
<!DOCTYPE html>
<html lang="en">
<head>
<meta charset="utf-8">
<title>Tot Petal — Tear Free Head-to-Toe Wash Label</title>
<link rel="stylesheet" href="https://fonts.googleapis.com/css2?family=Jost:wght@500;600;700&display=swap">
<style>
  :root {
    --backdrop: #d0d0d0;
    --label-white: #ffffff;
    --earth-brown: #9a7030;
    --tag-brown: #8f6a2e;
    --ink-black: #0b0b0b;
    --soft-skin: #f3dccb;
    --foam-blue: #cfe7f3;
  }
  html, body {
    margin: 0;
    padding: 0;
    width: 1200px;
    height: 1074px;
    overflow: hidden;
    background: var(--backdrop);
    font-family: "Jost", sans-serif;
  }
  .label {
    position: absolute;
    left: 248px;
    top: 31px;
    width: 704px;
    height: 1012px;
  }
  .label-shape {
    position: absolute;
    inset: 0;
  }
  .brand-mark {
    position: absolute;
    left: 254px;
    top: 34px;
    width: 196px;
    height: 196px;
    border: 2px solid var(--ink-black);
    border-radius: 50%;
    box-sizing: border-box;
    display: flex;
    align-items: center;
    justify-content: center;
  }
  .brand-name {
    font-weight: 600;
    font-size: 30px;
    letter-spacing: 3px;
    color: var(--ink-black);
    text-transform: uppercase;
  }
  .hero-illustration {
    position: absolute;
    left: 212px;
    top: 264px;
    width: 284px;
    height: 340px;
    border-radius: 46% 46% 30% 30%;
    background: radial-gradient(ellipse at 50% 35%, var(--soft-skin) 0%, var(--foam-blue) 45%, rgba(160,120,60,0.85) 75%, rgba(154,112,48,0) 100%);
  }
  .pediatrician-badge {
    position: absolute;
    left: 532px;
    top: 430px;
    width: 96px;
    height: 96px;
    border-radius: 50%;
    background: var(--label-white);
    border: 3px solid var(--ink-black);
    box-sizing: border-box;
    box-shadow: 0 0 0 3px var(--label-white);
  }
  .product-title {
    position: absolute;
    left: 0;
    width: 704px;
    top: 612px;
    margin: 0;
    text-align: center;
    font-weight: 700;
    font-size: 45px;
    line-height: 40px;
    letter-spacing: 5px;
    color: var(--ink-black);
    text-transform: uppercase;
  }
  .audience-ribbon {
    position: absolute;
    left: 172px;
    top: 712px;
    width: 360px;
    height: 48px;
  }
  .audience-text {
    position: absolute;
    left: 172px;
    top: 712px;
    width: 360px;
    height: 44px;
    line-height: 44px;
    text-align: center;
    font-weight: 600;
    font-size: 22px;
    letter-spacing: 2.5px;
    color: var(--ink-black);
  }
  .claims {
    position: absolute;
    left: 0;
    top: 786px;
    width: 704px;
    display: flex;
    justify-content: center;
    gap: 64px;
  }
  .claim {
    width: 89px;
    text-align: center;
    color: var(--label-white);
  }
  .claim-icon {
    width: 88px;
    height: 88px;
    display: block;
    margin: 0 auto;
  }
  .claim-text {
    margin-top: 10px;
    font-weight: 500;
    font-size: 14px;
    line-height: 18px;
    letter-spacing: 1px;
  }
  .volume-tag {
    position: absolute;
    left: 274px;
    top: 946px;
    width: 156px;
    height: 38px;
  }
  .volume-text {
    position: absolute;
    left: 274px;
    top: 946px;
    width: 156px;
    line-height: 38px;
    text-align: center;
    font-weight: 700;
    font-size: 24px;
    letter-spacing: 1.5px;
    color: var(--label-white);
  }
</style>
</head>
<body>
  <main class="label">
    <svg class="label-shape" width="704" height="1012" viewBox="0 0 704 1012">
      <defs>
        <clipPath id="label-outline">
          <path d="M0 136 C0 40 60 0 180 0 L524 0 C644 0 704 40 704 136 L704 1012 L0 1012 Z"/>
        </clipPath>
      </defs>
      <g clip-path="url(#label-outline)">
        <rect width="704" height="1012" fill="var(--label-white)"/>
        <path fill="var(--earth-brown)" d="M0 506 L24 500 L40 504 L62 495 L90 500 L112 492 L140 498 L160 490 L186 497 L210 488 L240 494 L262 486 L300 492 L340 488 L380 494 L420 486 L460 493 L500 487 L540 495 L572 489 L600 497 L630 490 L660 498 L684 492 L704 499 L704 1012 L0 1012 Z"/>
        <rect y="732" width="704" height="280" fill="var(--ink-black)"/>
      </g>
    </svg>

    <div class="brand-mark"><span class="brand-name">Tot Petal</span></div>

    <div class="hero-illustration" role="img" aria-label="Illustration of a baby with soap foam bathing in a brown clawfoot tub"></div>

    <div class="pediatrician-badge" role="img" aria-label="Pediatrician developed badge"></div>

    <h1 class="product-title">Tear Free<br>Head-to-Toe Wash</h1>

    <svg class="audience-ribbon" viewBox="0 0 360 48">
      <polygon points="0,8 20,8 14,26 20,44 0,44 8,26" fill="var(--label-white)" stroke="var(--ink-black)" stroke-width="2"/>
      <polygon points="360,8 340,8 346,26 340,44 360,44 352,26" fill="var(--label-white)" stroke="var(--ink-black)" stroke-width="2"/>
      <polygon points="14,2 346,2 340,22 346,42 14,42 20,22" fill="var(--label-white)"/>
    </svg>
    <div class="audience-text">FOR BABIES &amp; INFANTS</div>

    <section class="claims">
      <div class="claim">
        <svg class="claim-icon" viewBox="0 0 88 88" aria-hidden="true">
          <circle cx="44" cy="44" r="41" fill="none" stroke="var(--label-white)" stroke-width="3"/>
          <path d="M38 24 H50 V36 L60 60 H28 L38 36 Z" fill="var(--label-white)"/>
        </svg>
        <div class="claim-text">PARABEN<br>FREE</div>
      </div>
      <div class="claim">
        <svg class="claim-icon" viewBox="0 0 88 88" aria-hidden="true">
          <circle cx="44" cy="44" r="41" fill="none" stroke="var(--label-white)" stroke-width="3"/>
          <path d="M39 20 H49 V38 L60 62 H28 L39 38 Z" fill="none" stroke="var(--label-white)" stroke-width="3"/>
          <path d="M33 52 H55 L59 61 H29 Z" fill="var(--label-white)"/>
        </svg>
        <div class="claim-text">SULFATE<br>FREE</div>
      </div>
      <div class="claim">
        <svg class="claim-icon" viewBox="0 0 88 88" aria-hidden="true">
          <circle cx="44" cy="44" r="41" fill="none" stroke="var(--label-white)" stroke-width="3"/>
          <rect x="40" y="28" width="8" height="8" fill="var(--label-white)"/>
          <circle cx="44" cy="50" r="13" fill="var(--label-white)"/>
          <circle cx="60" cy="26" r="5" fill="none" stroke="var(--label-white)" stroke-width="2"/>
        </svg>
        <div class="claim-text">FRAGRANCE<br>FREE</div>
      </div>
      <div class="claim">
        <svg class="claim-icon" viewBox="0 0 88 88" role="img" aria-label="Cruelty free icon">
          <circle cx="44" cy="44" r="41" fill="none" stroke="var(--label-white)" stroke-width="3"/>
          <circle cx="44" cy="46" r="20" fill="var(--label-white)" opacity="0.85"/>
        </svg>
        <div class="claim-text">CRUELTY<br>FREE</div>
      </div>
    </section>

    <svg class="volume-tag" viewBox="0 0 156 38" aria-hidden="true">
      <polygon points="0,0 156,0 146,19 156,38 0,38 10,19" fill="var(--tag-brown)"/>
    </svg>
    <div class="volume-text">500ML</div>
  </main>
</body>
</html>
```